Brisk Comet- Energy shot - ....Amazing Energy for Amazing people

To design a creative /unique logo and picture for Brisk Comet Energy/ energy shot product similar to Zippo Day energy shot...Berry flavor

I want the design to cover the entire bottle. in addition to Logo (Brisk Comet Energy )

So Brisk Comet Energy will be a competitor of Zippo Day energy and I want a creative,fantastic, attractive design to catch customers eyes, the product will be in similar size 2oz bottle (see attached image). This template is based on a common 2oz bottle size that measures exactly 114mm circumference x 83mm-85mm height (including cap ).
Please include At the top cap a Logo for: Brisk Comet...

Target Market(s)

Young, busy professionals, athletics

Industry/Entity Type

Product

Logo Text

Quorva Energy...Amazing Energy &Taste !

Requirements
Must have
• Creative exciting design...Quorva Energy...Fan
Nice to have
• Be a genius....Be creative...Be Amazing !

```html
<!DOCTYPE html>
<html lang="en">
<head>
<meta charset="utf-8">
<title>Brisk Comet Energy – Berry Energy Shot Label</title>
<link href="https://fonts.googleapis.com/css2?family=Archivo+Black&family=Open+Sans:wght@700&family=Titan+One&family=Tinos&display=swap" rel="stylesheet">
<style>
  :root {
    --canvas: #ffffff;
    --cap: #0c0c0c;
    --cap-text: #ffffff;
    --body-top: #a81e1c;
    --body-mid: #e9341c;
    --body-bottom: #f3851f;
    --gold-light: #ffe37a;
    --gold-dark: #d49a12;
    --claim-text: #ffffff;
    --tick: #1fd13a;
    --slogan: #2cff2c;
    --slogan-shadow: #0a0a0a;
    --wave-light: #2aa6e0;
    --wave-dark: #0a6fbf;
    --scene-dark: #140a06;
    --flavour-badge: #e0a15a;
    --flavour-text: #1c3a8a;
  }
  * { margin: 0; padding: 0; box-sizing: border-box; }
  html, body { width: 1200px; height: 1000px; overflow: hidden; background: var(--canvas); }
  .canvas { position: relative; width: 1200px; height: 1000px; }
  .bottle-art { position: absolute; inset: 0; }

  .cap-wordmark {
    position: absolute; left: 474px; top: 14px; width: 258px;
    font-family: "Archivo Black", sans-serif; color: var(--cap-text);
    font-size: 62px; line-height: 84px; text-align: center; letter-spacing: 0;
  }

  .energy-title {
    position: absolute; left: 434px; top: 236px;
    font-family: "Archivo Black", sans-serif; font-size: 62px; letter-spacing: 2px;
    line-height: 80px;
    background: linear-gradient(180deg, var(--gold-light) 0%, var(--gold-dark) 100%);
    -webkit-background-clip: text; background-clip: text; color: transparent;
  }

  .claims { position: absolute; left: 404px; top: 348px; list-style: none; }
  .claims li {
    display: flex; align-items: center; height: 44px;
    font-family: "Open Sans", sans-serif; font-weight: 700; font-size: 31px;
    color: var(--claim-text);
  }
  .claims .tick { width: 26px; height: 26px; margin-right: 3px; }

  .slogan {
    position: absolute; left: 412px; top: 582px; width: 190px; text-align: center;
    font-family: "Titan One", sans-serif; font-size: 32px; line-height: 56px;
    color: var(--slogan);
    text-shadow: 3px 3px 0 var(--slogan-shadow);
  }

  .duration-badge {
    position: absolute; left: 415px; top: 727px; width: 130px; height: 130px;
    display: flex; align-items: center; justify-content: center;
    font-family: "Open Sans", sans-serif; font-weight: 700; font-size: 22px; color: #fff;
  }

  .flavour-label {
    position: absolute; left: 606px; top: 896px; width: 96px; height: 36px;
    display: flex; align-items: center; justify-content: center;
    font-family: "Tinos", serif; font-size: 20px; color: var(--flavour-text);
  }
</style>
</head>
<body>
<main class="canvas">
  <svg class="bottle-art" width="1200" height="1000" viewBox="0 0 1200 1000">
    <defs>
      <linearGradient id="body-fill" x1="0" y1="0" x2="0" y2="1">
        <stop offset="0" stop-color="var(--body-top)"/>
        <stop offset="0.4" stop-color="var(--body-mid)"/>
        <stop offset="1" stop-color="var(--body-bottom)"/>
      </linearGradient>
      <radialGradient id="burst-glow" cx="0.5" cy="0.5" r="0.5">
        <stop offset="0" stop-color="#ff9a2a" stop-opacity="0.75"/>
        <stop offset="1" stop-color="#ff9a2a" stop-opacity="0"/>
      </radialGradient>
      <linearGradient id="scene-fill" x1="0" y1="0" x2="0" y2="1">
        <stop offset="0" stop-color="#140a06" stop-opacity="0"/>
        <stop offset="0.35" stop-color="#140a06" stop-opacity="0.45"/>
        <stop offset="0.7" stop-color="#140a06" stop-opacity="0.9"/>
        <stop offset="1" stop-color="#140a06" stop-opacity="1"/>
      </linearGradient>
      <linearGradient id="ring-outer" x1="0" y1="0" x2="1" y2="1">
        <stop offset="0" stop-color="#ffe100"/>
        <stop offset="0.35" stop-color="#36d646"/>
        <stop offset="0.65" stop-color="#2bb7ff"/>
        <stop offset="1" stop-color="#e43bd0"/>
      </linearGradient>
      <radialGradient id="badge-core" cx="0.5" cy="0.5" r="0.5">
        <stop offset="0" stop-color="#ffb347"/>
        <stop offset="1" stop-color="#f07a1c"/>
      </radialGradient>
      <linearGradient id="bolt-fill" x1="0" y1="0" x2="0" y2="1">
        <stop offset="0" stop-color="var(--gold-light)"/>
        <stop offset="1" stop-color="var(--gold-dark)"/>
      </linearGradient>
      <clipPath id="bottle-body-clip">
        <path d="M480 185 L728 185 C735 232 800 222 805 272 L805 950 Q805 992 700 992 L505 992 Q400 992 400 950 L400 272 C405 222 472 232 480 185 Z"/>
      </clipPath>
    </defs>

    <g class="bottle-body" clip-path="url(#bottle-body-clip)">
      <rect x="395" y="180" width="415" height="815" fill="url(#body-fill)"/>
      <ellipse cx="690" cy="480" rx="200" ry="180" fill="url(#burst-glow)"/>
      <path class="wave-back" fill="var(--wave-light)"
        d="M395 862 C420 850 430 890 460 880 C490 870 500 905 530 900 C555 896 560 930 600 925 L600 995 L395 995 Z"/>
      <path class="wave-front" fill="var(--wave-dark)"
        d="M395 900 C425 885 440 925 470 915 C500 905 515 940 545 935 C570 930 580 960 610 955 L610 995 L395 995 Z"/>
      <rect class="athlete-scene" role="img" aria-label="Silhouette of an athlete sprinting up onto a rocky peak"
        x="548" y="530" width="262" height="465" rx="40" fill="url(#scene-fill)"/>
    </g>

    <rect class="bottle-cap" x="474" y="10" width="258" height="180" rx="14" fill="var(--cap)"/>

    <polygon class="energy-bolt" fill="url(#bolt-fill)" stroke="#3a2400" stroke-width="1.5"
      points="752,248 733,292 750,292 738,350 774,282 757,282 773,248"/>

    <g class="duration-ring">
      <circle cx="480" cy="792" r="62" fill="none" stroke="url(#ring-outer)" stroke-width="6"/>
      <circle cx="480" cy="792" r="54" fill="url(#badge-core)" stroke="#e43bd0" stroke-width="5"/>
      <circle cx="480" cy="792" r="47" fill="none" stroke="#2fd9e6" stroke-width="3"/>
    </g>

    <ellipse class="flavour-badge" cx="654" cy="914" rx="46" ry="18" fill="var(--flavour-badge)"/>
  </svg>

  <div class="cap-wordmark">BRISK<br>COMET</div>

  <div class="energy-title">ENERGY</div>

  <ul class="claims">
    <li><svg class="tick" viewBox="0 0 26 26"><path d="M3 14 L9 21 L23 4" fill="none" stroke="var(--tick)" stroke-width="3.5" stroke-linecap="round" stroke-linejoin="round"/></svg>Instant Energy</li>
    <li><svg class="tick" viewBox="0 0 26 26"><path d="M3 14 L9 21 L23 4" fill="none" stroke="var(--tick)" stroke-width="3.5" stroke-linecap="round" stroke-linejoin="round"/></svg>Amazing Taste</li>
    <li><svg class="tick" viewBox="0 0 26 26"><path d="M3 14 L9 21 L23 4" fill="none" stroke="var(--tick)" stroke-width="3.5" stroke-linecap="round" stroke-linejoin="round"/></svg>No crash Later</li>
    <li><svg class="tick" viewBox="0 0 26 26"><path d="M3 14 L9 21 L23 4" fill="none" stroke="var(--tick)" stroke-width="3.5" stroke-linecap="round" stroke-linejoin="round"/></svg>0 calories</li>
    <li><svg class="tick" viewBox="0 0 26 26"><path d="M3 14 L9 21 L23 4" fill="none" stroke="var(--tick)" stroke-width="3.5" stroke-linecap="round" stroke-linejoin="round"/></svg>0 sugar</li>
  </ul>

  <p class="slogan">Turn On<br>Your Mojo !</p>

  <div class="duration-badge">24hrs</div>

  <div class="flavour-label">Berry</div>
</main>
</body>
</html>
```